Business Card design for law firm = Juriskite Australia

We are seeking a new design for our business cards.
We are keeping our logo, which is attached.
We need space for
Name
Title
Address is , which is
Level 14
82 Penhallow Street
Sydney NSW 2000
Phone :
Mobile :
Fax :
Email :
DX :
website www.juriskite.com.au

Industry/Entity Type

Law Firm / Banking and Finance

Contact Information for Business Card

We are seeking a new design for our business cards. We are keeping our logo. We need space for Name Title Address is Level 14 82 Penhallow Street Sydney NSW 2000 Phone Mobile Fax Email DX website www.juriskite.com.au

Colors
0054AA
0677BA
7BADD7
CADEEF
E8F1F8

Requirements
Must have
• see our website for general feel www.juriskite.com.au

```html
<!DOCTYPE html>
<html lang="en">
<head>
<meta charset="utf-8">
<title>Juriskite Australia – Business Card</title>
<link rel="stylesheet" href="https://fonts.googleapis.com/css2?family=Crimson+Text&family=Open+Sans:wght@400&display=swap">
<style>
  :root {
    --stage: #1f1f1f;
    --brand-blue: #0677BA;
    --accent-cyan: #00A6DC;
    --paper: #ffffff;
    --serif: "Crimson Text", Georgia, serif;
    --sans: "Open Sans", Arial, sans-serif;
  }
  * { box-sizing: border-box; margin: 0; padding: 0; }
  html, body { width: 1200px; height: 1015px; overflow: hidden; background: var(--stage); }
  .stage { position: relative; width: 1200px; height: 1015px; }
  .card {
    position: absolute; left: 250px; width: 700px; height: 400px; overflow: hidden;
    box-shadow: 0 10px 30px rgba(0,0,0,.55);
  }
  .card-front { top: 85px; background: var(--brand-blue); }
  .card-back { top: 530px; background: var(--paper); }

  .brand-name {
    position: absolute; font-family: var(--serif); font-weight: 400;
    line-height: 1; white-space: nowrap;
  }
  .card-front .brand-name {
    left: 50%; top: 50%; transform: translate(-50%, -50%);
    font-size: 66px; color: var(--paper);
  }
  .card-back .brand-name {
    left: 161px; top: 142px; transform: translateX(-50%);
    font-size: 52px; color: var(--brand-blue);
  }

  .accent-band {
    position: absolute; left: 0; right: 0; top: 296px; height: 38px;
    background: var(--accent-cyan);
  }
  .info-panel {
    position: absolute; right: 0; top: 0; width: 54%; height: 296px;
    background: var(--brand-blue); color: var(--paper);
    padding: 38px 20px 0 38px; font-family: var(--sans);
  }
  .info-base {
    position: absolute; right: 0; top: 334px; width: 54%; height: 66px;
    background: var(--brand-blue);
  }
  .person-name { font-family: var(--serif); font-weight: 400; font-size: 34px; line-height: 1; }
  .person-title { font-size: 15px; margin-top: 4px; }
  .contact-list { list-style: none; margin-top: 14px; }
  .contact-list li { display: flex; align-items: center; gap: 10px; font-size: 15px; line-height: 22px; }
  .contact-list svg { width: 15px; height: 15px; flex: none; }
  .address { margin-top: 4px; padding-left: 25px; font-size: 15px; line-height: 22px; }
  .dx-number {
    position: absolute; left: 46%; top: 296px; height: 38px; padding-left: 38px;
    font-family: var(--sans); font-size: 15px; line-height: 38px; color: var(--paper);
  }
</style>
</head>
<body>
<main class="stage">
  <section class="card card-front" aria-label="Card front">
    <span class="brand-name">Juriskite</span>
  </section>

  <section class="card card-back" aria-label="Card back">
    <div class="accent-band"></div>
    <span class="brand-name">Juriskite</span>
    <div class="info-panel">
      <h1 class="person-name">Daniel Hartley</h1>
      <p class="person-title">Managing Director</p>
      <ul class="contact-list">
        <li><svg viewBox="0 0 16 16" fill="none" stroke="#fff" stroke-width="1.6"><path d="M3 2l3 1 1 3-2 1.5a8 8 0 004 4L10.5 9.5l3 1 .5 3-2 1C7 14 2 9 2 4z"/></svg>02-9555 0147</li>
        <li><svg viewBox="0 0 16 16" fill="none" stroke="#fff" stroke-width="1.6"><rect x="4" y="1.5" width="8" height="13" rx="1.5"/><path d="M7 12h2"/></svg>0491 570 238</li>
        <li><svg viewBox="0 0 16 16" fill="#fff"><rect x="4" y="1" width="8" height="5"/><rect x="1" y="6" width="14" height="6" rx="1"/><rect x="4" y="10" width="8" height="5" fill="#0677BA" stroke="#fff"/></svg>02-9555 0148</li>
        <li><svg viewBox="0 0 16 16" fill="none" stroke="#fff" stroke-width="1.6"><rect x="1.5" y="3.5" width="13" height="9"/><path d="M1.5 3.5L8 9l6.5-5.5"/></svg>info@juriskite.com.au</li>
        <li><svg viewBox="0 0 16 16" fill="none" stroke="#fff" stroke-width="1.4"><circle cx="8" cy="8" r="6.5"/><path d="M1.5 8h13M8 1.5c-3 3.5-3 9.5 0 13M8 1.5c3 3.5 3 9.5 0 13"/></svg>www.juriskite.com.au</li>
      </ul>
      <p class="address">Level 14, 82 Penhallow Street<br>Sydney NSW 2000</p>
    </div>
    <div class="info-base"></div>
    <p class="dx-number">DX:556 Sydney</p>
  </section>
</main>
</body>
</html>
```